Personal Development Book for Millennials Needs a Cover Design

Book Title: Salt Horizon: A Dreamer's Map to Being, 15 "No Escape" Queries on Joy, Routines and Grit for Muddled Millennials
Author's Name: Marcus T. Oldenfrey
Salt Horizon: A Dreamer's Map to Being is a collection of raw, unfiltered and personal essays on happiness, habits and hustle. It is a compilation of 15 provocative, yet fundamental questions that every mixed-up millennial or twenty-something should answer in order to live a life full of energy and excitement rather than monotony and mediocrity.
It is a personal development book written by a regular, twenty-something dude who got tired of doing boring things. He then quit his job, fell off a motorcycle somewhere near the equator, and came back to the States and immediately started writing.
"Pura vida," the law of the land in Costa Rica, translates to "pure life." "Pura vida" is more than just a greeting; it is an embodiment of the Costa Rican people, who find immense happiness in life's little pleasures, preferring to lay low, live slow and live purposefully. "Pura vida" is another way of saying "relax and take it easy."
The goal of the book is to stand out on the Zelvora platform as a small thumbnail. The imagery should make the viewer feel that the book (and the author) is an authority on the topic of self-discovery, self-awareness, and purposeful, intentional living.
The reader should feel that they MUST read this book if they are the least bit confused, anxious, mixed-up or desperately trying to figure out how to take back control of their own life and start doing the things that excite them. It's more important that the book "pops off the shelf" or stands out and catches the eye quickly.
The most important part of the design is that it is clean, uncluttered and simple. It should embody the "pura vida" lifestyle. I am open to any image or illustration you choose.
I like a bold color palette, and I'd like to see green be the primary color used in the design. Lush, greenery is everywhere in Costa Rica. Green also represents life, very appropriate for this book. I like bold titles that are easy to recognize and comprehend. Please use no more than 2-3 colors.
Zelvora eBook covers I particularly like:
Print Liftoff by Wesley Harrow
A Man Near The Pier by Neil Dorsey
Inner Steel — 48 Tested Paths to Build Inner Steel, Lift Your Morale and Quiet Inner Worry by Rory M.T. Pask
Hour Mastery: Peak Output by Owen Farrukh
Target Market(s)
Millennials
Requirements
Must have
- This book is intended to encourage millennials to do some soul-searching, think and WRITE down their own answers to the questions in this book. It is a book that should be read with a notebook and a pen close by.
- I'd like to see covers that subtly hint at this fact. Please reference the example covers listed in the project description to best match the style of cover I am looking for. If it is clear that you have NOT referenced the example covers, your design will be eliminated.
Nice to have
- If possible, would like to see designs that include the following three components WITHOUT making the cover feel too busy or cluttered:
- 1) Pen
- 2) Paper
- 3) Beach
Should not have
- Cover should NOT look or feel as if this is a book about environmentalism. Trees, plants, greenery, etc. should NOT be the primary focal point of the cover design. If included, these elements should be additive.

```html
<!DOCTYPE html>
<html lang="en">
<head>
<meta charset="utf-8">
<title>Salt Horizon: A Dreamer's Map to Being — Book Cover</title>
<link rel="stylesheet" href="https://fonts.googleapis.com/css2?family=Montserrat:wght@900&family=Oswald:wght@500;700&family=Roboto+Condensed:wght@400&display=swap">
<style>
  :root {
    --sky-top: #cfe5f6;
    --sky-low: #ffffff;
    --title-blue: #2b90e2;
    --leaf-green: #8dc63f;
    --ink: #111111;
    --band-blue: #2b90e2;
    --paper: #ffffff;
  }
  html, body {
    margin: 0;
    padding: 0;
    width: 703px;
    height: 1200px;
    overflow: hidden;
    background: var(--paper);
  }
  .cover {
    position: relative;
    width: 703px;
    height: 1200px;
    overflow: hidden;
    background: var(--paper);
  }
  .sky {
    position: absolute;
    left: 0;
    top: 0;
    width: 703px;
    height: 382px;
    background: linear-gradient(180deg, var(--sky-top) 0%, var(--sky-low) 100%);
  }
  .field {
    position: absolute;
    left: 0;
    top: 382px;
    width: 703px;
    height: 702px;
    background: var(--leaf-green);
  }
  .title {
    position: absolute;
    left: 0;
    top: 0;
    width: 703px;
    height: 580px;
  }
  .title text {
    font-family: "Montserrat", sans-serif;
    font-weight: 900;
  }
  .title .line-one { fill: var(--title-blue); }
  .title .line-two { fill: var(--paper); }
  .tagline {
    position: absolute;
    left: 0;
    top: 602px;
    width: 703px;
    margin: 0;
    text-align: center;
    font-family: "Oswald", sans-serif;
    font-weight: 700;
    font-size: 44px;
    line-height: 52px;
    letter-spacing: 0.5px;
    color: var(--ink);
    text-transform: uppercase;
  }
  .subtitle {
    position: absolute;
    left: 0;
    top: 742px;
    width: 703px;
    margin: 0;
    text-align: center;
    font-family: "Roboto Condensed", sans-serif;
    font-weight: 400;
    font-size: 38px;
    line-height: 52px;
    color: var(--ink);
  }
  .divider {
    position: absolute;
    left: 0;
    top: 1084px;
    width: 703px;
    height: 16px;
    background: var(--paper);
  }
  .author-band {
    position: absolute;
    left: 0;
    top: 1100px;
    width: 703px;
    height: 100px;
    background: var(--band-blue);
    display: flex;
    align-items: center;
    justify-content: center;
  }
  .author {
    margin: 0;
    font-family: "Oswald", sans-serif;
    font-weight: 500;
    font-size: 42px;
    letter-spacing: 1.5px;
    color: var(--paper);
    text-transform: uppercase;
  }
</style>
</head>
<body>
  <main class="cover">
    <div class="sky" role="img" aria-label="Pale blue sky with soft sunlight"></div>

    <div class="field"></div>

    <svg class="title" viewBox="0 0 703 580" role="heading" aria-level="1" aria-label="Salt Horizon">
      <text class="line-one" x="40" y="386" font-size="225" textLength="623" lengthAdjust="spacingAndGlyphs">SALT</text>
      <text class="line-two" x="40" y="556" font-size="205" textLength="623" lengthAdjust="spacingAndGlyphs">HORIZON</text>
    </svg>

    <p class="tagline">A Dreamer's Map to Being</p>

    <p class="subtitle">15 “No Escape” Queries<br>on Joy, Routines and Grit<br>for Muddled Millennials</p>

    <div class="divider"></div>

    <footer class="author-band">
      <p class="author">Marcus T. Oldenfrey</p>
    </footer>
  </main>
</body>
</html>
```